QM Fenwold Detailing, Inc.

I'm looking for business card design for an existing company with an existing logo/website. www.qmfenwold-detailing.com. VETERAN OWNED logo must be present.

Target Market(s)

Structural and architectural steel fabricators

Industry/Entity Type

Structural and architectural steel detailing and engineering

Contact Information for Business Card

logo, business name, address, phone, website, email, employee info

Font styles to use
Serif

Colors
00AB8E
00BBA5
67D7C9
C6EFE9
E9F9F6

Requirements
Must have
• company logo, website, VETERAN OWNED LOGO
Should not have
• Don't make it too busy. Less is more

```html
<!DOCTYPE html>
<html lang="en">
<head>
<meta charset="UTF-8">
<title>QM Fenwold Detailing — Business Card</title>
<link href="https://fonts.googleapis.com/css2?family=Open+Sans:wght@400;600;700&display=swap" rel="stylesheet">
<style>
  :root {
    --backdrop: #727272;
    --silver-light: #f1f2f4;
    --silver-mid: #d9dbde;
    --silver-dark: #c4c7cb;
    --teal-deep: #0d5f6c;
    --teal-mid: #1e8f9c;
    --teal-bright: #4fc6d0;
    --brand-teal: #1a9fb0;
    --text-light: #e6f1f3;
    --badge-red: #c8313a;
    --badge-blue: #1f4f8f;
  }
  * { margin: 0; padding: 0; box-sizing: border-box; }
  html, body { width: 1200px; height: 1000px; overflow: hidden; }
  body {
    background: var(--backdrop);
    font-family: "Open Sans", Arial, sans-serif;
    position: relative;
  }
  .card {
    position: absolute;
    left: 294px;
    width: 613px;
    height: 351px;
    border-radius: 14px;
    overflow: hidden;
  }
  .card--front {
    top: 119px;
    background: linear-gradient(100deg, var(--silver-mid) 0%, var(--silver-light) 35%, var(--silver-mid) 65%, var(--silver-dark) 100%);
  }
  .card--back {
    top: 520px;
    background: linear-gradient(95deg, var(--teal-deep) 0%, var(--teal-mid) 22%, var(--teal-bright) 40%, var(--teal-mid) 60%, var(--teal-deep) 80%, var(--teal-mid) 100%);
  }
  .brand-name {
    position: absolute;
    text-align: center;
    font-weight: 600;
    line-height: 1.1;
  }
  .card--front .brand-name {
    left: 0; right: 0;
    top: 118px;
    font-size: 38px;
    color: var(--brand-teal);
  }
  .card--back .brand-name {
    left: 84px;
    width: 200px;
    top: 122px;
    font-size: 28px;
    color: var(--text-light);
  }
  .veteran-badge { position: absolute; }
  .card--front .veteran-badge { left: 270px; top: 258px; }
  .card--back .veteran-badge { left: 154px; top: 242px; }
  .contact {
    position: absolute;
    left: 315px;
    top: 110px;
    color: var(--text-light);
    font-size: 13.5px;
    line-height: 19.5px;
  }
  .contact__name { font-weight: 700; font-size: 15px; letter-spacing: 0.3px; }
  .contact__title { font-size: 14px; margin-bottom: 11px; }
  .contact__company { font-weight: 700; font-size: 13px; }
  .contact__address { margin-bottom: 11px; }
  .contact__line { display: flex; align-items: center; gap: 7px; }
  .contact__line svg { width: 12px; height: 12px; flex: none; }
</style>
</head>
<body>

<section class="card card--front" aria-label="Card front">
  <div class="brand-name">QM Fenwold<br>Detailing</div>
  <svg class="veteran-badge" width="72" height="60" viewBox="0 0 72 60" role="img" aria-label="Veteran owned business badge">
    <rect x="8" y="4" width="56" height="52" rx="6" fill="var(--badge-blue)"/>
  </svg>
</section>

<section class="card card--back" aria-label="Card back">
  <div class="brand-name">QM Fenwold<br>Detailing</div>
  <svg class="veteran-badge" width="60" height="50" viewBox="0 0 60 50" role="img" aria-label="Veteran owned business badge">
    <rect x="6" y="3" width="48" height="44" rx="5" fill="var(--text-light)" opacity="0.85"/>
  </svg>

  <div class="contact">
    <div class="contact__name">NAME SURNAME</div>
    <div class="contact__title">Title</div>
    <div class="contact__company">QM Fenwold Detailing</div>
    <div class="contact__address">4815 Harbor Crest Ave., ste 310<br>Bayline, FL 33990</div>
    <div class="contact__line">
      <svg viewBox="0 0 12 12"><path d="M2.5 1h2l1 2.5-1.3 1a6.5 6.5 0 0 0 3.3 3.3l1-1.3L11 7.5v2A1.5 1.5 0 0 1 9.5 11 8.5 8.5 0 0 1 1 2.5 1.5 1.5 0 0 1 2.5 1z" fill="var(--text-light)"/></svg>
      555.204.7731
    </div>
    <div class="contact__line">
      <svg viewBox="0 0 12 12"><rect x="1" y="2.5" width="10" height="7" fill="var(--text-light)"/><path d="M1 2.5l5 4 5-4" fill="none" stroke="var(--teal-mid)" stroke-width="1"/></svg>
      sales@qmfenwold-detailing.com
    </div>
    <div class="contact__line">
      <svg viewBox="0 0 12 12"><g fill="none" stroke="var(--text-light)" stroke-width="1"><circle cx="6" cy="6" r="5"/><ellipse cx="6" cy="6" rx="2.2" ry="5"/><path d="M1 6h10"/></g></svg>
      www.qmfenwold-detailing.com
    </div>
  </div>
</section>

</body>
</html>
```